"Tales of Quiet Harbors" Book Cover Design

I am seeking a dynamic, modern, and professional cover design for a book focused on groundbreaking science that explores how a supplement called plasmalogens can revitalize the brain, prevent Alzheimer’s, and safeguard memories. The design should strike a balance between being visually appealing and conveying the seriousness of the topic.

Target Market(s)

The target audience includes individuals who are curious about cutting-edge science and proactive approaches to brain health, as well as those seeking to better understand how to protect their cognitive functions and memories. The cover should resonate with readers interested in health, science, and self-improvement, while reflecting the book’s informative and empowering tone.

Requirements
Must have
• The quotation across the top of the page (this is a placeholder for now, it will be changed eventually) and the author's name.
Should not have
• You don't need to use the puzzle idea!

```html
<!DOCTYPE html>
<html lang="en">
<head>
<meta charset="utf-8">
<title>Tales of Quiet Harbors — Cover Spread</title>
<link rel="stylesheet" href="https://fonts.googleapis.com/css2?family=League+Spartan:wght@700;800&family=Poppins:wght@400;500;600&family=Oswald:wght@300;400;600&family=Bebas+Neue&display=swap">
<style>
  :root {
    --stage-bg: #3f2149;
    --cover-bg: #f8e4fb;
    --ink: #2d1b31;
    --accent: #bf87cf;
    --art-light: #dcb8e6;
    --art-dark: #4a2c52;
    --photo-tone: #9a8f8c;
  }
  html, body {
    margin: 0;
    padding: 0;
    width: 792px;
    height: 1200px;
    overflow: hidden;
    background: var(--stage-bg);
  }
  .spread {
    position: absolute;
    left: 16px;
    top: 337px;
    width: 760px;
    height: 526px;
    background: var(--cover-bg);
    color: var(--ink);
    box-shadow: 0 6px 18px rgba(0,0,0,0.35);
    overflow: hidden;
  }
  .spread p, .spread h1, .spread h2, .spread h3 { margin: 0; }

  /* Back cover */
  .back-cover {
    position: absolute;
    left: 0;
    top: 0;
    width: 356px;
    height: 526px;
  }
  .back-title {
    position: absolute;
    left: 25px;
    top: 34px;
    font-family: "Bebas Neue", sans-serif;
    font-weight: 400;
    font-size: 44px;
    line-height: 37px;
    letter-spacing: -0.5px;
  }
  .back-title-lead { display: block; color: var(--ink); }
  .back-title-main { display: block; color: var(--accent); }
  .back-copy {
    position: absolute;
    left: 26px;
    width: 302px;
    font-family: "Poppins", sans-serif;
    font-size: 7.2px;
    line-height: 8.8px;
    color: var(--ink);
  }
  .back-copy-blurb { top: 121px; }
  .about-label {
    position: absolute;
    left: 25px;
    top: 279px;
    font-family: "Poppins", sans-serif;
    font-weight: 400;
    font-size: 13px;
    color: var(--accent);
    text-transform: uppercase;
  }
  .about-name {
    position: absolute;
    left: 25px;
    top: 294px;
    font-family: "League Spartan", sans-serif;
    font-weight: 800;
    font-size: 14px;
    text-transform: uppercase;
    color: var(--ink);
  }
  .about-name-credential { font-weight: 700; }
  .author-photo {
    position: absolute;
    left: 26px;
    top: 337px;
    width: 53px;
    height: 53px;
    background: linear-gradient(160deg, #cfcfcf 0%, var(--photo-tone) 60%, #2c2f3a 100%);
  }
  .back-copy-bio { left: 97px; top: 334px; width: 236px; }
  .back-copy-closing { top: 400px; }

  /* Spine */
  .spine {
    position: absolute;
    left: 356px;
    top: 0;
    width: 49px;
    height: 526px;
  }
  .spine-title {
    position: absolute;
    left: 33px;
    top: 22px;
    transform-origin: 0 0;
    transform: rotate(90deg);
    white-space: nowrap;
    font-family: "League Spartan", sans-serif;
    font-weight: 800;
    font-size: 16px;
    color: var(--ink);
    text-transform: uppercase;
  }
  .spine-author {
    position: absolute;
    left: 30px;
    top: 382px;
    transform-origin: 0 0;
    transform: rotate(90deg);
    white-space: nowrap;
    font-family: "Poppins", sans-serif;
    font-weight: 600;
    font-size: 8.5px;
    color: var(--accent);
    text-transform: uppercase;
  }

  /* Front cover */
  .front-cover {
    position: absolute;
    left: 405px;
    top: 0;
    width: 355px;
    height: 526px;
  }
  .cover-art {
    position: absolute;
    left: 160px;
    top: 36px;
    width: 178px;
    height: 266px;
    border-radius: 50% 46% 30% 40% / 40% 44% 20% 30%;
    background: linear-gradient(160deg, var(--art-dark) 0%, var(--accent) 55%, var(--art-light) 100%);
  }
  .endorsement {
    position: absolute;
    left: 27px;
    top: 26px;
    width: 130px;
    margin: 0;
  }
  .endorsement-mark { display: block; width: 34px; height: 22px; }
  .endorsement-text {
    margin-top: 12px !important;
    font-family: "Poppins", sans-serif;
    font-weight: 400;
    font-size: 13.5px;
    line-height: 16.8px;
  }
  .endorsement-source {
    margin-top: 6px !important;
    font-family: "Poppins", sans-serif;
    font-weight: 600;
    font-size: 8.5px;
  }
  .book-title {
    position: absolute;
    left: 26px;
    top: 228px;
    font-family: "League Spartan", sans-serif;
    font-weight: 800;
    text-transform: uppercase;
  }
  .book-title-lead {
    display: block;
    font-size: 48px;
    line-height: 37px;
    letter-spacing: -0.5px;
    color: var(--ink);
  }
  .book-title-main {
    display: block;
    margin-top: 4px;
    font-size: 74px;
    line-height: 58px;
    letter-spacing: -1px;
    color: var(--accent);
  }
  .author {
    position: absolute;
    left: 27px;
    top: 462px;
    font-family: "Oswald", sans-serif;
    font-size: 25px;
    letter-spacing: 1px;
    text-transform: uppercase;
    color: var(--ink);
  }
  .author-name { font-weight: 600; }
  .author-credential { font-weight: 300; }
</style>
</head>
<body>
  <main class="spread">
    <section class="back-cover">
      <h2 class="back-title">
        <span class="back-title-lead">Tales of</span>
        <span class="back-title-main">Quiet Harbors</span>
      </h2>
      <p class="back-copy back-copy-blurb">Lorem ipsum dolor sit amet, consectetur adipiscing elit, sed do eiusmod tempor incididunt ut labore et dolore magna aliqua. Quis ipsum suspendisse ultrices gravida. Risus commodo viverra maecenas accumsan lacus vel facilisis. Lorem ipsum dolor sit amet, consectetur adipiscing elit, sed do eiusmod tempor incididunt ut labore et dolore magna aliqua. Quis ipsum suspendisse ultrices gravida. Risus commodo viverra maecenas accumsan lacus vel facilisis. Lorem ipsum dolor sit amet, consectetur adipiscing elit, sed do eiusmod tempor incididunt ut labore et dolore magna aliqua. Quis ipsum suspendisse ultrices gravida. Risus commodo viverra maecenas accumsan lacus vel facilisis. Lorem ipsum dolor sit amet, consectetur adipiscing elit, sed do eiusmod tempor incididunt ut labore et dolore magna aliqua. Quis ipsum suspendisse ultrices gravida. Risus commodo viverra maecenas accumsan lacus vel facilisis. Lorem ipsum dolor sit amet, consectetur adipiscing elit, sed do eiusmod tempor incididunt ut labore et dolore magna aliqua. Quis ipsum suspendisse ultrices gravida. Risus commodo viverra maecenas accumsan lacus vel facilisis.</p>
      <p class="about-label">About</p>
      <h3 class="about-name">Daniel Ashford, <span class="about-name-credential">MD</span></h3>
      <div class="author-photo" role="img" aria-label="Author portrait photograph"></div>
      <p class="back-copy back-copy-bio">Lorem ipsum dolor sit amet, consectetur adipiscing elit, sed do eiusmod tempor incididunt ut labore et dolore magna aliqua. Quis ipsum suspendisse ultrices gravida. Risus commodo viverra maecenas accumsan lacus vel facilisis. Lorem ipsum dolor sit amet, consectetur adipiscing elit, sed do eiusmod tempor incididunt ut labore et dolore magna aliqua. Quis ipsum suspendisse ultrices gravida.</p>
      <p class="back-copy back-copy-closing">Lorem ipsum dolor sit amet, consectetur adipiscing elit, sed do eiusmod tempor incididunt ut labore et dolore magna aliqua. Quis ipsum suspendisse ultrices gravida. Risus commodo viverra maecenas accumsan lacus vel facilisis. Lorem ipsum dolor sit amet, consectetur adipiscing elit, sed do eiusmod tempor incididunt ut labore et dolore magna aliqua. Quis ipsum suspendisse ultrices gravida.</p>
    </section>

    <section class="spine">
      <p class="spine-title">Tales of Quiet Harbors</p>
      <p class="spine-author">Daniel Ashford, MD</p>
    </section>

    <section class="front-cover">
      <div class="cover-art" role="img" aria-label="Cover illustration: stylised profile of a person with eyes closed in lilac and deep plum tones"></div>

      <blockquote class="endorsement">
        <svg class="endorsement-mark" viewBox="0 0 78 54" aria-hidden="true">
          <circle cx="18" cy="34" r="17" fill="#bf87cf"/>
          <path d="M4 32 C4 14 14 4 30 2 L30 10 C20 13 15 20 15 30 Z" fill="#bf87cf"/>
          <circle cx="58" cy="34" r="17" fill="#bf87cf"/>
          <path d="M44 32 C44 14 54 4 70 2 L70 10 C60 13 55 20 55 30 Z" fill="#bf87cf"/>
        </svg>
        <p class="endorsement-text">An<br>incredible<br>guide to<br>protecting<br>your<br>mind and<br>memories.</p>
        <p class="endorsement-source">- Dr Leena Varma, MD</p>
      </blockquote>

      <h1 class="book-title">
        <span class="book-title-lead">Tales of</span>
        <span class="book-title-lead">Quiet</span>
        <span class="book-title-main">Harbors</span>
      </h1>

      <p class="author"><span class="author-name">Daniel Ashford,</span> <span class="author-credential">MD</span></p>
    </section>
  </main>
</body>
</html>
```